Business Card

We would like a very clean corporate, two sided business card that conveys that we are a quality focused, reliable organisation that can make a business better. We focus on a cycle of continuous improvement for IT systems.

The brief is primarily clean and corporate, nothing overly complicated.

We sell IT services, IT support, server implementation, problem solving services to businesses in Australia.

Business

```html
<!DOCTYPE html>
<html lang="en">
<head>
<meta charset="utf-8">
<title>Mendline – Business Card</title>
<link rel="stylesheet" href="https://fonts.googleapis.com/css2?family=Exo+2:wght@500&family=Roboto:wght@300;400;700&family=Roboto+Condensed:wght@900&display=swap">
<style>
  :root {
    --backdrop: #dcdcdc;
    --card-white: #ffffff;
    --ink-navy: #2a2c3e;
    --brand-pink: #e3115a;
    --pink-deep: #c90f4c;
    --pink-light: #ef2a72;
    --accent-coral: #e0606b;
    --rule-grey: #c8c8c8;
    --muted-grey: #8a8a8a;
    --text-white: #ffffff;
    --text-black: #111111;
  }
  * { box-sizing: border-box; margin: 0; padding: 0; }
  html, body {
    width: 799px; height: 1200px; overflow: hidden;
    background: var(--backdrop);
  }
  .sheet { position: relative; width: 799px; height: 1200px; }
  .card {
    position: absolute; overflow: hidden;
    background: var(--card-white);
  }
  .card--front-plain { left: 147px; top: 95px; width: 520px; height: 298px; }
  .card--front-pattern { left: 141px; top: 444px; width: 528px; height: 301px; }
  .card--back { left: 143px; top: 812px; width: 522px; height: 296px; }
  .fill { position: absolute; inset: 0; }
  .fill--front {
    background: radial-gradient(ellipse 62% 58% at 62% 48%,
      var(--card-white) 0%, var(--card-white) 62%,
      var(--pink-light) 88%, var(--brand-pink) 100%);
  }
  .fill--back {
    background: linear-gradient(135deg, var(--pink-deep) 0%, var(--brand-pink) 55%, var(--pink-light) 100%);
  }

  .brand {
    position: absolute; display: flex; align-items: center; gap: 22px;
  }
  .brand__name {
    font-family: "Exo 2", sans-serif; font-weight: 500;
    font-size: 62px; line-height: 1; color: var(--ink-navy);
    letter-spacing: 0.5px;
  }
  .brand__dot {
    width: 26px; height: 26px; border-radius: 50%;
    background: var(--accent-coral);
  }
  .card--front-plain .brand { left: 58px; top: 100px; }
  .card--front-pattern .brand { left: 55px; top: 106px; }

  .tagline {
    position: absolute; width: 148px; border-top: 1px solid var(--rule-grey);
    padding-top: 3px; text-align: center;
    font-family: "Roboto", sans-serif; font-size: 13px; font-weight: 300;
    color: var(--muted-grey); letter-spacing: -0.2px;
  }
  .tagline strong { font-weight: 700; color: var(--ink-navy); }
  .card--front-plain .tagline { left: 173px; top: 217px; }
  .card--front-pattern .tagline { left: 163px; top: 208px; }

  .contact {
    position: absolute; left: 25px; top: 142px;
    font-family: "Roboto", sans-serif; color: var(--text-white);
  }
  .contact__name { font-size: 17px; font-weight: 400; letter-spacing: 0.3px; line-height: 20px; }
  .contact__role {
    font-family: "Roboto Condensed", sans-serif; font-weight: 900;
    font-size: 14px; color: var(--text-black); line-height: 16px; margin-bottom: 8px;
  }
  .contact__line { font-size: 15px; line-height: 20px; }
  .contact__line b { font-weight: 700; display: inline-block; width: 14px; }
</style>
</head>
<body>
<main class="sheet">

  <section class="card card--front-plain" aria-label="Card front, plain">
    <div class="brand">
      <span class="brand__name">mendline</span>
      <span class="brand__dot"></span>
    </div>
    <p class="tagline"><strong>IT</strong> SERVICES</p>
  </section>

  <section class="card card--front-pattern" aria-label="Card front, patterned">
    <div class="fill fill--front" role="img" aria-label="Pink faceted pattern area surrounding a white centre"></div>
    <div class="brand">
      <span class="brand__name">mendline</span>
      <span class="brand__dot"></span>
    </div>
    <p class="tagline"><strong>IT</strong> SERVICES</p>
  </section>

  <section class="card card--back" aria-label="Card back">
    <div class="fill fill--back" role="img" aria-label="Pink faceted pattern background"></div>
    <div class="contact">
      <p class="contact__name">DANIEL REYES</p>
      <p class="contact__role">YOUR POSITION</p>
      <p class="contact__line"><b>P</b>: +61 555 0100</p>
      <p class="contact__line"><b>E</b>: yourname@yourdomain.com</p>
      <p class="contact__line"><b>W</b>: www.yourwebsite.com</p>
    </div>
  </section>

</main>
</body>
</html>
```